Harrowgate Estates Business Card for Apartment Buildings

Create business cards for resident managers who run apartment buildings. The audience is the public who are searching for apartment rentals, and current residents who live at the apartment building. Key design element will be incorporating the company logo, however, the logo cannot dominate. The building name and manager name are more important than the logo. Current business card design leaves little room for copy, so we may need to reduce the size on the current card to allow for more space for copy.

Target Market(s)

Adults 18-65 years of age, who are looking for an apartment rental, plus current residents who live at our apartment buildings.

Industry/Entity Type

Property Management

Contact Information for Business Card

A major design element will be use of the company logo. Important property and manager contact information must be part of the design. The size of the logo will need to be reduced to make room for building and manager contact copy.

Font styles to use
Sans Serif

Colors
3176b5
000000
959595
ffffff

Requirements
Must have
• 1) Incorporate the company logo.
• 2) Use the company colors (dark blue, black/grey, over white).
• 3) FEATURE THE BUILDING NAME
• 4) FEATURE THE MANAGER NAME
• 5) The company name is less important than BUILDING and MANAGER
• 6) Manager contact information
• **SEE ATTACHED CREATIVE BRIEF**
Nice to have
• 1) Back of card logo watermark
• 2) Ability to write notes on back of carfd
Should not have
• Avoid letting the company logo dominate the card, the building name and manager are more important than the company logo.

```html
<!DOCTYPE html>
<html lang="en">
<head>
<meta charset="utf-8">
<title>Linden Court Apartments – Business Card</title>
<link rel="stylesheet" href="https://fonts.googleapis.com/css2?family=Arimo:wght@400;700&display=swap">
<style>
  :root {
    --brand-blue: #3176b5;
    --ink: #000000;
    --grey: #959595;
    --dark-grey: #4a4a4a;
    --paper: #ffffff;
    --backdrop: #e9e9ea;
  }
  * { box-sizing: border-box; margin: 0; padding: 0; }
  html, body {
    width: 1200px; height: 1000px; overflow: hidden;
    background: var(--backdrop);
    font-family: "Arimo", Arial, sans-serif;
  }
  .sheet {
    width: 1200px; height: 1000px;
    display: flex; flex-direction: column; align-items: center; justify-content: center;
    gap: 60px;
  }
  .card {
    position: relative;
    width: 700px; height: 400px;
    background: var(--paper);
    box-shadow: 0 6px 20px rgba(0,0,0,.15);
    overflow: hidden;
  }
  /* Front */
  .building { position: absolute; left: 48px; top: 40px; }
  .building-name {
    color: var(--brand-blue); font-weight: 700; font-size: 40px; letter-spacing: .5px;
    white-space: nowrap;
  }
  .building-address {
    color: var(--dark-grey); font-size: 17px; margin-top: 4px; padding-left: 64px;
    white-space: nowrap;
  }
  .company-mark {
    position: absolute; left: 48px; top: 232px;
    display: flex; align-items: center; gap: 10px;
  }
  .company-mark .square { width: 20px; height: 20px; background: var(--brand-blue); flex: none; }
  .company-mark .name { color: var(--dark-grey); font-weight: 700; font-size: 20px; white-space: nowrap; }
  .divider {
    position: absolute; left: 292px; top: 140px; width: 3px; height: 210px;
    background: var(--brand-blue);
  }
  .manager { position: absolute; left: 320px; top: 135px; }
  .manager-name { color: var(--brand-blue); font-weight: 700; font-size: 30px; white-space: nowrap; }
  .manager-title { color: var(--dark-grey); font-size: 16px; margin-top: 2px; }
  .contact {
    margin-top: 16px; display: grid; grid-template-columns: 66px auto;
    row-gap: 10px; font-size: 18px;
  }
  .contact dt { color: var(--dark-grey); font-weight: 700; white-space: nowrap; }
  .contact dd { color: var(--dark-grey); white-space: nowrap; }
  /* Back */
  .watermark {
    position: absolute; left: 0; right: 0; top: 165px; text-align: center;
    color: var(--brand-blue); opacity: .12; font-weight: 700; font-size: 56px;
    white-space: nowrap;
  }
  .notes { position: absolute; left: 50px; right: 50px; top: 48px; }
  .note-line { height: 38px; border-bottom: 3px dotted var(--brand-blue); }
</style>
</head>
<body>
<main class="sheet">
  <section class="card card-front">
    <header class="building">
      <h1 class="building-name">Linden Court Apartments</h1>
      <p class="building-address">2485 Larkspur Avenue, San Diego, CA 92104</p>
    </header>
    <div class="company-mark">
      <span class="square"></span>
      <span class="name">Harrowgate Estates</span>
    </div>
    <div class="divider"></div>
    <div class="manager">
      <h2 class="manager-name">Marisol Quintero</h2>
      <p class="manager-title">Resident Manager</p>
      <dl class="contact">
        <dt>Office</dt><dd>: 555-214-3870.</dd>
        <dt>Cell</dt><dd>: 555-368-9142.</dd>
        <dt>Fax</dt><dd>: 555-402-6615.</dd>
        <dt>Email</dt><dd>: marisol@harrowgateest.com.</dd>
      </dl>
    </div>
  </section>

  <section class="card card-back">
    <div class="watermark">Harrowgate Estates</div>
    <div class="notes">
      <div class="note-line"></div>
      <div class="note-line"></div>
      <div class="note-line"></div>
      <div class="note-line"></div>
      <div class="note-line"></div>
      <div class="note-line"></div>
      <div class="note-line"></div>
      <div class="note-line"></div>
    </div>
  </section>
</main>
</body>
</html>
```